Redesign an App Mockup for Messaging app

I want one page redesigned for my app & 1 icon built from scratch.

I also want a few simple color changes on 5 of the other pages.

i can help you get the changes right, you can message me on Skype: Torvim82

first person finished wins the contest

```html
<!DOCTYPE html>
<html lang="en">
<head>
<meta charset="utf-8">
<title>Community Service – Group Chat</title>
<link rel="stylesheet" href="https://fonts.googleapis.com/css2?family=Roboto:wght@400;500;700&display=swap">
<style>
  :root {
    --page-bg: #e8eef3;
    --brand-teal: #3aabc3;
    --brand-teal-dark: #319bb2;
    --surface: #ffffff;
    --text-main: #333a3f;
    --text-muted: #9a9fa3;
    --name-teal: #3aa6bf;
    --tick-green: #6cb32e;
    --divider: #c9ced2;
    --avatar-john: #c9a98c;
    --avatar-alex: #8a6a55;
    --avatar-lily: #a98a76;
  }
  * { box-sizing: border-box; margin: 0; padding: 0; }
  html, body {
    width: 876px; height: 1200px; overflow: hidden;
    background: var(--page-bg);
    font-family: "Roboto", "Helvetica Neue", Arial, sans-serif;
  }
  .screen {
    position: absolute; left: 108px; top: 11px;
    width: 440px; height: 785px;
    transform: scale(1.5); transform-origin: top left;
    background: var(--surface);
    overflow: hidden;
  }
  .top-bar {
    position: absolute; left: 0; top: 0; width: 440px; height: 88px;
    background: var(--brand-teal); color: #fff;
  }
  .status-bar { position: absolute; left: 0; top: 0; width: 100%; height: 28px; font-size: 14px; }
  .status-carrier { position: absolute; left: 8px; top: 6px; display: flex; align-items: center; gap: 4px; }
  .signal-dots { display: flex; gap: 2px; }
  .signal-dots span { width: 6px; height: 6px; border-radius: 50%; background: #fff; }
  .status-time { position: absolute; left: 0; right: 0; top: 6px; text-align: center; font-weight: 700; font-size: 15px; }
  .status-battery { position: absolute; right: 8px; top: 9px; width: 32px; height: 12px; border: 1px solid #fff; border-radius: 3px; padding: 1px; }
  .status-battery::before { content: ""; display: block; width: 100%; height: 100%; background: #fff; border-radius: 1px; }
  .status-battery::after { content: ""; position: absolute; right: -4px; top: 3px; width: 2px; height: 4px; background: #fff; }
  .header-back { position: absolute; left: 26px; top: 45px; }
  .header-title { position: absolute; left: 0; right: 0; top: 45px; display: flex; justify-content: center; align-items: center; gap: 8px; font-size: 22px; font-weight: 400; }

  .message { position: absolute; left: 0; width: 440px; top: var(--top); }
  .avatar { position: absolute; left: 5px; top: 0; width: 46px; height: 46px; border-radius: 50%; }
  .avatar-john { background: radial-gradient(circle at 50% 40%, #e6cdb6, var(--avatar-john)); }
  .avatar-alex { background: radial-gradient(circle at 50% 40%, #c7a088, var(--avatar-alex)); }
  .avatar-lily { background: radial-gradient(circle at 50% 45%, #e3c6b3, var(--avatar-lily)); }
  .sender { position: absolute; left: 60px; top: 0; font-size: 18px; font-weight: 700; color: var(--name-teal); }
  .meta { position: absolute; right: 9px; top: 3px; display: flex; align-items: center; gap: 10px; font-size: 14px; color: var(--text-muted); }
  .body { position: absolute; left: 60px; top: 25px; width: 360px; font-size: 17.5px; line-height: 23px; color: var(--text-main); }
  .attachment { position: absolute; left: 59px; top: 104px; display: flex; align-items: center; gap: 12px; font-size: 16px; color: #7c8387; }

  .composer-divider { position: absolute; left: 17px; top: 655px; width: 405px; height: 1px; background: var(--divider); }
  .composer-placeholder { position: absolute; left: 0; right: 0; top: 674px; text-align: center; font-size: 18px; color: var(--text-muted); }
  .toolbar {
    position: absolute; left: 0; top: 725px; width: 440px; height: 60px;
    background: var(--brand-teal);
  }
  .tool { position: absolute; top: 0; height: 60px; display: flex; align-items: center; }
  .tool-send { right: 13px; color: #fff; font-size: 18px; }
</style>
</head>
<body>
<main class="screen">
  <header class="top-bar">
    <div class="status-bar">
      <div class="status-carrier">
        <div class="signal-dots"><span></span><span></span><span></span><span></span><span></span></div>
        <span>Norvia</span>
        <svg width="16" height="12" viewBox="0 0 16 12" fill="none" stroke="#fff" stroke-width="1.8" stroke-linecap="round"><path d="M1.5 4.5a9.5 9.5 0 0 1 13 0"/><path d="M4 7.3a6 6 0 0 1 8 0"/><circle cx="8" cy="10.3" r="1" fill="#fff" stroke="none"/></svg>
      </div>
      <div class="status-time">11:57 AM</div>
      <div class="status-battery"></div>
    </div>
    <svg class="header-back" width="16" height="28" viewBox="0 0 16 28" fill="none" stroke="#fff" stroke-width="3.2" stroke-linecap="round" stroke-linejoin="round"><path d="M13 2 2 14l11 12"/></svg>
    <h1 class="header-title">
      <svg width="28" height="20" viewBox="0 0 28 20" fill="none" stroke="#fff" stroke-width="1.4"><circle cx="14" cy="6" r="3.5"/><path d="M7.5 18c0-4 3-6.5 6.5-6.5s6.5 2.5 6.5 6.5z"/><circle cx="6" cy="6.5" r="2.8"/><path d="M1 16c0-3 2.2-5 5-5"/><circle cx="22" cy="6.5" r="2.8"/><path d="M27 16c0-3-2.2-5-5-5"/></svg>
      <span>Community Service</span>
    </h1>
  </header>

  <section class="conversation">
    <article class="message" style="--top:98px">
      <div class="avatar avatar-john" role="img" aria-label="Profile photo of John"></div>
      <h2 class="sender">John</h2>
      <div class="meta"><svg width="13" height="10" viewBox="0 0 13 10" fill="none" stroke="var(--tick-green)" stroke-width="2"><path d="M1 5l4 4 7-8"/></svg>11:55 AM</div>
      <p class="body">That'd be awesome. Do you have any details worked out?</p>
    </article>

    <article class="message" style="--top:182px">
      <div class="avatar avatar-alex" role="img" aria-label="Profile photo of Alex"></div>
      <h2 class="sender">Alex</h2>
      <div class="meta"><svg width="13" height="10" viewBox="0 0 13 10" fill="none" stroke="var(--tick-green)" stroke-width="2"><path d="M1 5l4 4 7-8"/></svg>11:55 AM</div>
      <p class="body">Here's what I've got so far. Please mind that it's confidential, but I think you guys are integral part of this.</p>
      <div class="attachment">
        <svg width="38" height="48" viewBox="0 0 38 48" fill="none" stroke="var(--brand-teal)" stroke-width="1.6"><path d="M2 2h24l10 10v34H2z"/><path d="M26 2v10h10"/><rect x="6" y="26" width="26" height="13" rx="2"/><text x="19" y="36" text-anchor="middle" font-family="Roboto, sans-serif" font-size="9" fill="var(--brand-teal)" stroke="none">XLS</text></svg>
        <span>ProspectResearch.xls</span>
      </div>
    </article>

    <article class="message" style="--top:357px">
      <div class="avatar avatar-lily" role="img" aria-label="Profile photo of Lily"></div>
      <h2 class="sender">Lily</h2>
      <div class="meta"><svg width="13" height="10" viewBox="0 0 13 10" fill="none" stroke="var(--tick-green)" stroke-width="2"><path d="M1 5l4 4 7-8"/></svg>11:56 AM</div>
      <p class="body">Thanks for sharing! Let's see if either one of us can provide them with any insightful tips.</p>
    </article>

    <article class="message" style="--top:468px">
      <div class="avatar avatar-john" role="img" aria-label="Profile photo of John"></div>
      <h2 class="sender">John</h2>
      <div class="meta"><svg width="13" height="10" viewBox="0 0 13 10" fill="none" stroke="var(--tick-green)" stroke-width="2"><path d="M1 5l4 4 7-8"/></svg>11:56 AM</div>
      <p class="body">Sure thing. How's Amy by the way?</p>
    </article>

    <article class="message" style="--top:536px">
      <div class="avatar avatar-alex" role="img" aria-label="Profile photo of Alex"></div>
      <h2 class="sender">Alex</h2>
      <div class="meta"><svg width="13" height="10" viewBox="0 0 13 10" fill="none" stroke="var(--tick-green)" stroke-width="2"><path d="M1 5l4 4 7-8"/></svg>11:57 AM</div>
      <p class="body">She's doing great, I'll tell her you said hi</p>
    </article>

    <article class="message" style="--top:601px">
      <div class="avatar avatar-lily" role="img" aria-label="Profile photo of Lily"></div>
      <h2 class="sender">Lily</h2>
      <div class="meta"><svg width="13" height="10" viewBox="0 0 13 10" fill="none" stroke="var(--tick-green)" stroke-width="2"><path d="M1 5l4 4 7-8"/></svg>11:57 AM</div>
      <p class="body">Yes, please do</p>
    </article>
  </section>

  <div class="composer-divider"></div>
  <div class="composer-placeholder">Tap to start a message</div>

  <nav class="toolbar">
    <div class="tool" style="left:15px">
      <svg width="40" height="32" viewBox="0 0 40 32" fill="#fff"><path d="M4 7h8l3-5h10l3 5h8a3 3 0 0 1 3 3v18a3 3 0 0 1-3 3H4a3 3 0 0 1-3-3V10a3 3 0 0 1 3-3z"/><circle cx="20" cy="18" r="8" fill="var(--brand-teal)"/><circle cx="20" cy="18" r="5.5"/><rect x="5" y="3.5" width="5" height="2.5"/></svg>
    </div>
    <div class="tool" style="left:102px">
      <svg width="42" height="34" viewBox="0 0 42 34" fill="#fff"><path d="M17 2C8 2 2 8 2 15c0 6 5 10 10 9 3-.5 3 2 3 4 0 3 3 4 6 3 9-2 14-8 14-15C35 8 27 2 17 2z"/><circle cx="10" cy="13" r="2.5" fill="var(--brand-teal)"/><circle cx="16" cy="8" r="2.5" fill="var(--brand-teal)"/><circle cx="24" cy="9" r="2.5" fill="var(--brand-teal)"/><circle cx="27" cy="16" r="2.5" fill="var(--brand-teal)"/><path d="M35 24v9M30.5 28.5h9" stroke="#fff" stroke-width="2.2"/></svg>
    </div>
    <div class="tool" style="left:182px">
      <svg width="34" height="34" viewBox="0 0 34 34"><path d="M1 2h32v24H14l-6 6v-6H1z" fill="#fff"/><text x="17" y="21" text-anchor="middle" font-family="Roboto, sans-serif" font-size="18" fill="var(--brand-teal)">A</text></svg>
    </div>
    <div class="tool" style="left:297px">
      <svg width="42" height="42" viewBox="0 0 42 42" fill="none" stroke="#fff" stroke-width="2.4"><circle cx="21" cy="21" r="19"/><path d="M21 8v13h-9" stroke-linecap="round"/></svg>
    </div>
    <div class="tool tool-send">Send</div>
  </nav>
</main>
</body>
</html>
```